Wedding dance company needs flyer design

I am looking for a double sided A5 flyer to be designed for my company Step Quill.

The concept of the flyer is to attract couples for their first wedding dance.

This is to support content of our website: http://www.stepquillgroup.example/bridal-set

All the text content for the flyer is attached in flyer.txt. My company logo is attached in logo.zip.

I would like to have 1-2 photos on the flyer based on a couple and their wedding first dance and perhaps some designs without photos (graphics instead).

```html
<!DOCTYPE html>
<html lang="en">
<head>
<meta charset="utf-8">
<title>Step Quill – First Dance Flyer</title>
<link rel="stylesheet" href="https://fonts.googleapis.com/css2?family=Oswald:wght@300;400&family=Open+Sans:wght@400;700&family=EB+Garamond:wght@500&display=swap">
<style>
  :root {
    --ink: #111111;
    --paper: #f2f2f2;
    --magenta: #e0138c;
    --plum: #7a1478;
    --white: #ffffff;
    --text: #1b1b1b;
  }
  html, body { margin: 0; padding: 0; width: 1200px; height: 924px; overflow: hidden; background: #dcdcdc; }
  .flyer {
    position: absolute; left: 60px; top: 80px; width: 1080px; height: 763px;
    background: var(--paper); overflow: hidden;
    box-shadow: 0 4px 18px rgba(0,0,0,.25);
  }
  .dark-panel { position: absolute; left: 0; top: 0; width: 1080px; height: 763px; }
  .dancers {
    position: absolute; left: 292px; top: 282px; width: 190px; height: 352px;
    background: linear-gradient(115deg, #ffffff 0%, #c4c4c4 40%, #1a1a1a 100%);
  }

  .hook { position: absolute; left: 0; top: 0; width: 360px; height: 540px; font-family: "Oswald", sans-serif; font-weight: 300; color: var(--white); }
  .hook-line { position: absolute; white-space: nowrap; line-height: 1; transform-origin: left top; }
  .hook-line.pink { color: var(--magenta); }
  .line-feeling  { left: 59px; top: 24px;  font-size: 61px;  transform: scaleX(.71); }
  .line-nervous  { left: 17px; top: 42px;  font-size: 105px; font-weight: 400; transform: scaleX(.77); }
  .line-about    { left: 224px; top: 122px; font-size: 54px;  transform: scaleX(.69); }
  .line-your     { left: 175px; top: 155px; font-size: 64px;  font-weight: 400; transform: scaleX(.97); }
  .line-first    { left: 46px; top: 212px; font-size: 72px;  transform: scaleX(.82); }
  .line-then     { left: 46px; top: 320px; font-size: 42px;  transform: scaleX(.74); }
  .line-name     { left: 46px; top: 358px; font-size: 72px;  transform: scaleX(.82); }
  .line-care     { left: 46px; top: 431px; font-size: 38px;  transform: scaleX(.82); }
  .line-planning { left: 46px; top: 484px; font-size: 38px;  transform: scaleX(.82); }

  .social { position: absolute; left: 40px; top: 698px; font-family: "Open Sans", sans-serif; font-weight: 700; font-size: 14px; color: var(--white); line-height: 27px; }

  .pitch { position: absolute; right: 23px; top: 12px; width: 680px; text-align: right; font-family: "Open Sans", sans-serif; font-weight: 700; color: var(--text); }
  .pitch h1 { margin: 0; font-size: 25.5px; line-height: 36px; }
  .pitch h2 { margin: 9px 0 0; font-size: 21px; line-height: 28px; }
  .story { position: absolute; left: 505px; top: 213px; width: 556px; margin: 0; font-family: "Open Sans", sans-serif; font-size: 16px; line-height: 22.5px; text-align: justify; color: var(--text); }

  .packages { position: absolute; left: 483px; top: 355px; width: 597px; height: 217px;
    background: linear-gradient(90deg, var(--plum) 0%, var(--magenta) 35%, var(--magenta) 100%);
    font-family: "EB Garamond", serif; font-weight: 500; color: var(--white); text-align: center; }
  .packages-title { height: 35px; line-height: 37px; font-size: 24px; letter-spacing: 2px; background: var(--magenta); box-shadow: 0 3px 4px rgba(0,0,0,.3); }
  .package { width: 410px; margin: 0 0 0 115px; font-size: 25.5px; line-height: 28px; padding: 6px 0 4px; border-bottom: 1px solid rgba(255,255,255,.85); letter-spacing: .3px; }
  .package:last-child { border-bottom: 0; line-height: 25px; }
  .extras { position: absolute; left: 510px; top: 573px; width: 566px; margin: 0; text-align: center; font-family: "Open Sans", sans-serif; font-size: 11.7px; color: var(--text); }

  .brand { position: absolute; left: 620px; top: 615px; width: 370px; text-align: center; font-family: "Open Sans", sans-serif; font-weight: 700; font-size: 30px; color: var(--magenta); line-height: 40px; }
  .brand::before { content: ""; display: inline-block; width: 10px; height: 10px; background: var(--magenta); margin-right: 10px; vertical-align: middle; }
  .contact { position: absolute; left: 520px; width: 570px; text-align: center; font-family: "Open Sans", sans-serif; color: var(--text); }
  .tel { top: 664px; font-size: 24px; font-weight: 700; }
  .email { top: 700px; font-size: 16.5px; }
  .web { top: 728px; font-size: 17px; font-weight: 700; color: var(--magenta); letter-spacing: 9px; }
</style>
</head>
<body>
<main class="flyer">
  <svg class="dark-panel" viewBox="0 0 1080 763" aria-hidden="true">
    <polygon points="0,0 360,0 360,494 519,763 0,763" fill="var(--ink)"/>
  </svg>
  <div class="dancers" role="img" aria-label="Silhouette of a couple dancing a ballroom first dance"></div>

  <div class="hook">
    <span class="hook-line line-feeling">Are you feeling</span>
    <span class="hook-line pink line-nervous">nervous</span>
    <span class="hook-line line-about">about</span>
    <span class="hook-line line-your">your</span>
    <span class="hook-line pink line-first">first dance?</span>
    <span class="hook-line line-then">Then why not let</span>
    <span class="hook-line pink line-name">Step Quill</span>
    <span class="hook-line line-care">take care of all the</span>
    <span class="hook-line line-planning">planning for you!</span>
  </div>
  <div class="social">
    Chirper - @StepQuillCo<br>
    Chatterbook- chatterbook.example/stepquillevents
  </div>

  <section class="pitch">
    <h1>Step Quill specialise in preparing couples for their<br>first dance to ensure it’s memorable.</h1>
    <h2>Lessons can take place in a studio of your choice<br>or in the comfort of your own home.<br>We provide a wide range of dance styles and<br>various packages to suit all budgets.</h2>
  </section>
  <p class="story">Step Quill, a small family business, provide flexibility and personal touches to make you feel comfortable and confident on the dance floor. Whether you want simple steps, a classic Waltz or a glitzy extravaganza, you'll soon be able to wow your friends and family. Your bespoke first wedding dance will match your song, natural style and ability, so it will never be too difficult and will suit you perfectly.</p>

  <section class="packages">
    <div class="packages-title">PACKAGES (STARTING AT £65)</div>
    <div class="package">Bronze Package – 1 x 1 hour lesson</div>
    <div class="package">Silver Package – 1 x 90 minute lesson</div>
    <div class="package">Gold Package - 2 x 90 minute lessons</div>
    <div class="package">Platinum Package - 1 x 2 hour lesson<br>and 2 x 90 minute lessons</div>
  </section>
  <p class="extras">We also offer the SOS last minute package, on-site rehearsals, hen parties and gift vouchers.</p>

  <div class="brand">Step Quill</div>
  <div class="contact tel">Tel- 07700900418 / 07700900419</div>
  <div class="contact email">Email- info@stepquillgroup.example</div>
  <div class="contact web">www.stepquillgroup.example</div>
</main>
</body>
</html>
```